HOBBY CARD COLLECTIBLE STICKER & FOILD PACKAGING DESIGN

Project Overview:
We are a trading company specializing in selling hobby cards for sports enthusiasts worldwide. We are launching a new series of trading cards featuring popular sports such as GLX (basketball), TQR (baseball), VKD (football), ZOPE/RoMeta/OKTU (soccer), and JPH (wrestling). Our customers will be able to purchase these cards online from our website.

We are launching a series of hobby cards for JPH, American Football, Baseball, Basketball, and Moon Tides. We need a design for the packaging and sticker on the packaging box that will appeal to our target audience and showcase the collectible cards.

Target Audience:
The target audience for the hobby cards is collectors, enthusiasts, and casual buyers of all ages. The packaging should be designed to appeal to a wide range of customers.

Branding:
The overall brand message that we want to convey through the packaging is one of excitement, exclusivity, and fun. The packaging should highlight our brand values of quality, authenticity, and innovation.

Theme:
Each of the hobby card collections has a unique theme - JPH, American Football, Baseball, Basketball, and Moon Tides. We will need to create a silhoutte design for each theme that looks like they're a part of the same series. Essentially, the designs need to look like they belong in the same design family. The packaging design should incorporate the key elements associated with each theme, such as silhouttes of wrestlers for JPH, helmets for American Football, bats and balls for Baseball, basketballs and hoops for Basketball, and Moon Tides characters for Moon Tides without infringing copyright.

We need designs for the trading card foil packaging and box sticker. The designs should reflect the respective sports and must incorporate official colors used in the sports. Please conduct research on the official colors used by each sport to ensure accuracy. We require silhouette illustrations that accurately reflect the sports mentioned above.

Layout:
The packaging will be a black rigid box(12.7 x 7.6 x 5 cm). The sticker design will be on the box. The foil packaging of the hobby cards are (7x 10 cm). Information that needs to be included on the sticker and foil packaging includes our brand name, product name, and any legal or regulatory information.

Artwork:
The artwork on the packaging will be silhouttes of the themes. The artwork should be consistent with the overall branding and theme of the product.

Restrictions:
Please note that we require the designs to use a maximum of three colors to maintain consistency with our branding. Kindly ensure that the proposed designs are eye-catching, visually appealing, and will appeal to sports enthusiasts. Thank you.

Deliverables:
The design brief should include the following deliverables:

Sticker and Foil Packaging design concepts for each theme (JPH, American Football, Baseball, Basketball, and Moon Tides) that looks together
Final packaging designs for each theme
Mockups of the packaging designs
Final WORKING artwork files for the packaging designs in AI,PSD,JPEG,PDF
Printing specifications and guidelines

Target Market(s)

Card Collectors that have an interest in collecting Sports(JPH, VKD, GLX, TRQ, Soccer)

Font styles to use
Serif
Sans Serif
Decorative

Colors

Designer to choose colors to be used in the design.

Requirements
Must have
• Must use only official sports colors like the Blue, Red and White for VKD (to keep within 3 colors)
Nice to have
• Silhouttes of respective genres, same art style as FOOTBALL sample design (refer to attached files)
Should not have
• No more than 3 colors in proposed design including background

```html
<!DOCTYPE html>
<html lang="en">
<head>
<meta charset="utf-8">
<title>Halvard Hobby Collectibles – Foil Pack Series</title>
<link rel="stylesheet" href="https://fonts.googleapis.com/css2?family=Cinzel:wght@500&family=Oswald:wght@500&display=swap">
<style>
  :root {
    --page: #ffffff;
    --foil-light: #2a66c4;
    --foil-mid: #164a9e;
    --foil-dark: #0b2d6b;
    --ink: #ffffff;
    --ink-blue: #1030b0;
    --football: #ff1010;
    --baseball: #f4f80a;
    --basketball: #f07818;
    --soccer: #22e4f0;
    --wrestling: #1fe21f;
  }
  * { margin: 0; padding: 0; box-sizing: border-box; }
  html, body { width: 1200px; height: 1145px; overflow: hidden; background: var(--page); }
  .series { position: relative; width: 1200px; height: 1145px; }

  .pack {
    position: absolute;
    width: 422px;
    height: 292px;
    background:
      radial-gradient(ellipse 60% 55% at 45% 45%, var(--foil-light) 0%, var(--foil-mid) 55%, var(--foil-dark) 100%);
    overflow: hidden;
  }
  .pack--football   { left: 155px; top: 98px;  --accent: var(--football); }
  .pack--baseball   { left: 613px; top: 98px;  --accent: var(--baseball); }
  .pack--basketball { left: 155px; top: 421px; --accent: var(--basketball); }
  .pack--soccer     { left: 613px; top: 421px; --accent: var(--soccer); }
  .pack--wrestling  { left: 385px; top: 744px; --accent: var(--wrestling); }

  .pack__art {
    position: absolute;
    left: 58px; top: 76px;
    width: 100px; height: 100px;
    border-radius: 50%;
    background: radial-gradient(circle, rgba(255,255,255,0.55) 0%, rgba(255,255,255,0.18) 70%, rgba(255,255,255,0) 100%);
  }
  .pack__divider {
    position: absolute;
    left: 166px; top: 82px;
    width: 2px; height: 84px;
    background: var(--accent);
  }
  .pack__brand {
    position: absolute;
    left: 178px; top: 82px;
    font-family: "Cinzel", serif;
    font-weight: 500;
    font-size: 24px;
    line-height: 27px;
    color: var(--ink);
    letter-spacing: 0.5px;
  }
  .pack__band {
    position: absolute;
    left: 0; top: 192px;
    width: 100%; height: 25px;
    background: var(--accent);
    display: flex; align-items: center;
    padding-left: 62px;
  }
  .pack__tagline {
    font-family: "Oswald", sans-serif;
    font-weight: 500;
    font-size: 15px;
    letter-spacing: 2.6px;
    color: var(--ink);
  }
  .pack--baseball .pack__tagline { color: var(--ink-blue); }
  .pack--soccer .pack__band { padding-left: 64px; }
</style>
</head>
<body>
<main class="series">

  <section class="pack pack--football">
    <div class="pack__art" role="img" aria-label="White silhouette of an American football player in helmet carrying a red ball"></div>
    <span class="pack__divider"></span>
    <p class="pack__brand">Halvard<br>Hobby<br>Collectibles</p>
    <div class="pack__band"><span class="pack__tagline">“HALVARD CURATED WONDERS!”</span></div>
  </section>

  <section class="pack pack--baseball">
    <div class="pack__art" role="img" aria-label="White silhouette of a baseball batter swinging a yellow bat"></div>
    <span class="pack__divider"></span>
    <p class="pack__brand">Halvard<br>Hobby<br>Collectibles</p>
    <div class="pack__band"><span class="pack__tagline">“HALVARD CURATED WONDERS!”</span></div>
  </section>

  <section class="pack pack--basketball">
    <div class="pack__art" role="img" aria-label="White outline silhouette of a basketball player dribbling, with orange accents"></div>
    <span class="pack__divider"></span>
    <p class="pack__brand">Halvard<br>Hobby<br>Collectibles</p>
    <div class="pack__band"><span class="pack__tagline">“HALVARD CURATED WONDERS!”</span></div>
  </section>

  <section class="pack pack--soccer">
    <div class="pack__art" role="img" aria-label="White silhouette of a soccer player kicking a ball"></div>
    <span class="pack__divider"></span>
    <p class="pack__brand">Halvard<br>Hobby<br>Collectibles</p>
    <div class="pack__band"><span class="pack__tagline">“HALVARD CURATED WONDERS!”</span></div>
  </section>

  <section class="pack pack--wrestling">
    <div class="pack__art" role="img" aria-label="White silhouette of two wrestlers grappling, with green accents"></div>
    <span class="pack__divider"></span>
    <p class="pack__brand">Halvard<br>Hobby<br>Collectibles</p>
    <div class="pack__band"><span class="pack__tagline">“HALVARD CURATED WONDERS!”</span></div>
  </section>

</main>
</body>
</html>
```